Business card: GREEN HERONS TRADE SUPPLY

Hello,

This is your mission:

-I've just done my logo on the website. Now, I need A BUSINESS CARD.
-2 same business cards for 2 persons
-Landscape
-Dimension of the business card: 8.5 cm long and 5 cm high
-Different front and back
-For your information: this new company is selling products (fashion accessories, electronics, watches, fragrances, sunglasses, etc. to large clients related to shops in airlines (inflight catalogue), airports, cruises, etc.
-Colors and logo: please use the same colors of the logo attached (in blue with orange details) and follow the spirit of the existing logo.

-Front:
-1st person:
GREEN HERONS s.p.r.l.
Travel Retail Agency
www.greenheronsco.example
Lucien MARTOLIER
Partner
Mobile: +32480627315
Email: lm@greenheronsco.example
-2nd person:
GREEN HERONS s.p.r.l.
Travel Retail Agency
www.greenheronsco.example
Joris VANDERHOLME
Partner
Mobile: +32486153702
Email: jv@greenheronsco.example

-Back
Logo
see attached file. Please use the colors of the logo in blue with orange details.

Reason: I increase time necause i don t know if the deadline is in usa time or european time. I will make the selection at 9pm belgian time.

I'm selling products to large accounts/clients. Some of them do more than 2 Billion eur turnover

Airlines

Must have
• Use the logo.
The buyers get so many business cards.
They should remember me easily.
This is why my logo/company name is a stork and a color. 2 things that people usually remember easily.

```html
<!DOCTYPE html>
<html lang="en">
<head>
<meta charset="utf-8">
<title>Green Herons Trade Supply – Business Card</title>
<link href="https://fonts.googleapis.com/css2?family=Questrial&display=swap" rel="stylesheet">
<style>
  :root {
    --backdrop: #e4e4e4;
    --card-white: #ffffff;
    --navy: #0d4a86;
    --teal: #1190b8;
    --orange: #f08a2c;
    --ink: #2b2b2b;
  }
  html, body {
    margin: 0;
    width: 1200px;
    height: 750px;
    overflow: hidden;
    background: radial-gradient(circle at 40% 35%, #f1f1f1, var(--backdrop));
    font-family: "Questrial", sans-serif;
  }
  .cards {
    position: absolute;
    inset: 0;
    display: flex;
    gap: 60px;
    align-items: center;
    justify-content: center;
  }
  .card {
    position: relative;
    width: 500px;
    height: 294px;
    border-radius: 18px;
    overflow: hidden;
    background: var(--card-white);
    box-shadow: 0 10px 28px rgba(0,0,0,0.18);
  }
  .card-shapes {
    position: absolute;
    inset: 0;
    width: 100%;
    height: 100%;
  }
  .brand-name {
    position: absolute;
    margin: 0;
    color: var(--navy);
    font-size: 22px;
    letter-spacing: 2px;
    font-weight: 400;
    line-height: 1.15;
  }
  .card-back .brand-name {
    right: 34px;
    top: 52px;
    width: 220px;
    text-align: center;
  }
  .card-front .brand-name {
    left: 36px;
    top: 70px;
    width: 240px;
  }
  .holder-name {
    position: absolute;
    left: 36px;
    top: 148px;
    margin: 0;
    color: var(--orange);
    font-size: 20px;
    font-weight: 400;
  }
  .contact-list {
    position: absolute;
    left: 36px;
    top: 190px;
    margin: 0;
    padding: 0;
    list-style: none;
    color: var(--ink);
    font-size: 15px;
  }
  .contact-list li {
    display: flex;
    align-items: center;
    gap: 10px;
    height: 28px;
  }
  .contact-icon {
    width: 18px;
    height: 18px;
    flex: none;
  }
</style>
</head>
<body>
  <main class="cards">
    <!-- Back side -->
    <section class="card card-back" aria-label="Business card back">
      <svg class="card-shapes" viewBox="0 0 500 294" aria-hidden="true">
        <rect width="500" height="294" fill="var(--navy)"/>
        <circle cx="385" cy="-30" r="235" fill="var(--teal)"/>
        <circle cx="395" cy="-40" r="215" fill="var(--card-white)"/>
      </svg>
      <p class="brand-name">GREEN HERONS<br>TRADE SUPPLY</p>
    </section>

    <!-- Front side -->
    <section class="card card-front" aria-label="Business card front">
      <svg class="card-shapes" viewBox="0 0 500 294" aria-hidden="true">
        <path d="M150,294 C300,294 330,70 500,22 L500,294 Z" fill="var(--teal)"/>
        <path d="M205,294 C340,288 370,95 500,62 L500,294 Z" fill="var(--navy)"/>
      </svg>
      <p class="brand-name">GREEN HERONS<br>TRADE SUPPLY</p>
      <h1 class="holder-name">Lucien MARTOLIER</h1>
      <ul class="contact-list">
        <li>
          <svg class="contact-icon" viewBox="0 0 18 18" aria-hidden="true">
            <circle cx="9" cy="9" r="9" fill="var(--orange)"/>
            <rect x="6" y="4" width="6" height="10" rx="1.2" fill="none" stroke="#fff" stroke-width="1.4"/>
          </svg>
          <span>+32480627315</span>
        </li>
        <li>
          <svg class="contact-icon" viewBox="0 0 18 18" aria-hidden="true">
            <circle cx="9" cy="9" r="9" fill="var(--orange)"/>
            <rect x="4.5" y="6" width="9" height="6.5" rx="1" fill="none" stroke="#fff" stroke-width="1.3"/>
            <path d="M4.8,6.4 L9,9.6 L13.2,6.4" fill="none" stroke="#fff" stroke-width="1.3"/>
          </svg>
          <span>lm@greenheronsco.example</span>
        </li>
      </ul>
    </section>
  </main>
</body>
</html>
```